Dental Office Needs Exciting New Stationary

We need a stationary design that incorporates the logo that we already have and would like to keep the existing color scheme. We need something clean and professional. This is a Endodontic (root canals) office and must represent a dental specialist's office. I need a design for a business card, envelope, and letterhead that all coordinate. I would like the business card to incorporate the information in the business card sample that I am providing. I made the business card design myself but would like to see a better one.

```html
<!DOCTYPE html>
<html lang="en">
<head>
<meta charset="utf-8">
<title>Meridian Endodontics — Business Card</title>
<link href="https://fonts.googleapis.com/css2?family=Open+Sans:wght@300;400;600&display=swap" rel="stylesheet">
<style>
  :root {
    --backdrop: #c9d5db;
    --paper: #ffffff;
    --brand-blue: #1f73c8;
    --tab-blue: #2a86d4;
    --ink: #6b6e72;
    --ink-soft: #8a8d91;
    --divider: #c4c7cb;
  }
  * { box-sizing: border-box; margin: 0; padding: 0; }
  html, body {
    width: 1200px; height: 1000px; overflow: hidden;
    background: var(--backdrop);
    font-family: "Open Sans", sans-serif;
  }
  .card {
    position: absolute;
    width: 540px; height: 310px;
    background: var(--paper);
    box-shadow: 0 6px 14px rgba(40, 60, 70, 0.18);
  }
  .card--front { left: 150px; top: 150px; }
  .card--back { left: 510px; top: 560px; }

  /* Front */
  .brand {
    position: absolute; inset: 0;
    display: flex; align-items: center; justify-content: center; gap: 16px;
  }
  .brand__dot {
    width: 30px; height: 30px; border-radius: 50%;
    background: var(--brand-blue);
  }
  .brand__rule { width: 1px; height: 46px; background: var(--divider); }
  .brand__name {
    font-weight: 600; font-size: 24px; letter-spacing: 0.5px;
    color: var(--brand-blue);
  }

  /* Back */
  .tab {
    position: absolute; right: 0; top: 0;
    width: 210px; height: 42px;
    background: var(--tab-blue);
    display: flex; align-items: center; gap: 8px;
    padding-left: 18px;
  }
  .tab__dot { width: 12px; height: 12px; border: 2px solid #fff; border-radius: 50%; }
  .tab__name { color: #fff; font-weight: 600; font-size: 11px; letter-spacing: 0.3px; }
  .contact {
    position: absolute;
    display: flex; align-items: center; gap: 5px;
    font-size: 8px; color: var(--ink);
  }
  .contact svg { width: 8px; height: 8px; fill: var(--tab-blue); flex: none; }
  .contact-list { position: absolute; display: flex; flex-direction: column; gap: 5px; }
  .contact-list .contact { position: static; }
  .web { right: 58px; top: 50px; }
  .phones { left: 320px; top: 196px; }
  .faxes { right: 22px; top: 168px; }
  .addresses { left: 22px; bottom: 22px; }
  .doctors {
    position: absolute; left: 170px; top: 140px;
    font-weight: 300; font-size: 19px; line-height: 1.3; color: var(--ink);
  }
</style>
</head>
<body>

<section class="card card--front" aria-label="Business card front">
  <div class="brand">
    <span class="brand__dot"></span>
    <span class="brand__rule"></span>
    <span class="brand__name">Meridian Endodontics</span>
  </div>
</section>

<section class="card card--back" aria-label="Business card back">
  <div class="tab">
    <span class="tab__dot"></span>
    <span class="tab__name">Meridian Endodontics</span>
  </div>

  <div class="contact web">
    <svg viewBox="0 0 10 10"><circle cx="5" cy="5" r="4"/></svg>
    www.meridianendo.com
  </div>

  <div class="doctors">
    <p>Daniel R. Whitcomb DDS MS</p>
    <p>Marco L. Estevan DDS</p>
  </div>

  <div class="contact-list phones">
    <div class="contact">
      <svg viewBox="0 0 10 10"><path d="M2 1l2 0 1 2-1 1c.6 1.2 1.4 2 2.6 2.6l1-1 2 1v2c0 .6-.4 1-1 1C4 9.6.4 6 .4 2c0-.6.4-1 1-1z"/></svg>
      555.310.2366
    </div>
    <div class="contact">
      <svg viewBox="0 0 10 10"><path d="M2 1l2 0 1 2-1 1c.6 1.2 1.4 2 2.6 2.6l1-1 2 1v2c0 .6-.4 1-1 1C4 9.6.4 6 .4 2c0-.6.4-1 1-1z"/></svg>
      555.310.1801
    </div>
  </div>

  <div class="contact-list faxes">
    <div class="contact">
      <svg viewBox="0 0 10 10"><rect x="1" y="3" width="8" height="5" rx="1"/><rect x="3" y="1" width="4" height="2"/></svg>
      555.310.5909
    </div>
    <div class="contact">
      <svg viewBox="0 0 10 10"><rect x="1" y="3" width="8" height="5" rx="1"/><rect x="3" y="1" width="4" height="2"/></svg>
      555.310.0602
    </div>
  </div>

  <div class="contact-list addresses">
    <div class="contact">
      <svg viewBox="0 0 10 10"><path d="M5 0a3.5 3.5 0 0 1 3.5 3.5C8.5 6 5 10 5 10S1.5 6 1.5 3.5A3.5 3.5 0 0 1 5 0z"/></svg>
      1480 Birch Street, Fairview, Ca 95010
    </div>
    <div class="contact">
      <svg viewBox="0 0 10 10"><path d="M5 0a3.5 3.5 0 0 1 3.5 3.5C8.5 6 5 10 5 10S1.5 6 1.5 3.5A3.5 3.5 0 0 1 5 0z"/></svg>
      3720 Lake Ave, Suite #2, Oakridge, Ca 95020
    </div>
  </div>
</section>

</body>
</html>
```